Sports Fishing Charter Costa Rica Website

We have a fishing charter business in Costa Rica. I have tried to build the website, but because of our needs it is far beyond my knowledge. I have currently been using WordPress, which I've paid for so I'd like to keep. With that said I'd like someone to go into it and start from scratch or tweak what is there. We would like to have a calendar that a customer can look at, pick a date, see if it's available, choose the type of charter they want, book, and pay. Informative on the fishing in Costa Rica, specifically out of Quepos. Fishing seasons, about the boat/equipment, calendar, trip options/pricing, fishing reports, contact info, social media links, local tournament options with links to the registration. We offer full day off shore, 3/4 day offshore, 1/2 day inshore, 1/2 day cruise (morning snorkel or sunset). The final should be user friendly and easy to maintain. *The logo is currently being updated.

Target Market(s)

people that like to fish and people on vacation in Costa Rica

Industry/Entity Type

fishing

Number of Pages Required

1 page

Font styles to use
Sans Serif

Colors
0054AA
0677BA
7BADD7
CADEEF
E8F1F8

Requirements
Must have
• a calendar that shows month to month what dates are available and the customer can choose the type of charter, book, and pay

```html
<!DOCTYPE html>
<html lang="en">
<head>
<meta charset="utf-8">
<title>Sports Fishing Charter Costa Rica</title>
<link rel="stylesheet" href="https://fonts.googleapis.com/css2?family=IBM+Plex+Sans:wght@600;700&family=Open+Sans:wght@400;600;700&display=swap">
<style>
:root{
  --navy:#0054AA;
  --blue:#0677BA;
  --sky:#7BADD7;
  --mist:#CADEEF;
  --ice:#E8F1F8;
  --ink:#111;
  --grey:#f5f5f5;
  --muted:#a8a8a8;
}
*{margin:0;padding:0;box-sizing:border-box}
html,body{width:1200px;height:4637px;overflow:hidden;background:#fff}
body{position:relative;font-family:"Open Sans",sans-serif;color:var(--ink)}
.abs{position:absolute}
.head-font{font-family:"IBM Plex Sans",sans-serif;font-weight:700}
.btn{position:absolute;display:flex;align-items:center;justify-content:center;border-radius:999px;font-family:"IBM Plex Sans",sans-serif;font-weight:700;color:#fff;background:linear-gradient(90deg,var(--navy),var(--blue));letter-spacing:.5px}
.photo{position:absolute;overflow:hidden}

/* header */
.topbar{left:0;top:0;width:1200px;height:90px;background:#fff}
.phone{left:150px;top:28px;display:flex;align-items:center;gap:10px;font-family:"IBM Plex Sans",sans-serif;font-weight:700;font-size:20px;color:var(--navy)}
.phone-dot{width:34px;height:34px;border-radius:50%;background:var(--blue);display:flex;align-items:center;justify-content:center}
.brand{left:0;width:1200px;top:24px;text-align:center;font-size:31px;color:var(--navy);letter-spacing:.5px}
.brand span{color:var(--blue)}
.mainnav{left:0;top:90px;width:1200px;height:47px;background:var(--navy)}
.mainnav ul,.footnav ul{list-style:none;display:flex;justify-content:space-between;position:absolute;left:151px;width:898px}
.mainnav ul{top:15px}
.mainnav li{color:#fff;font-size:12.5px}
.mainnav li.active{font-weight:700;text-decoration:underline}

/* hero */
.hero{left:0;top:137px;width:1200px;height:580px;background:linear-gradient(180deg,#1b8de6 0%,#0b6cc8 40%,#0a58b0 75%,#0d4f9e 100%)}
.hero-title{left:0;width:1200px;top:252px;text-align:center;color:#fff;font-size:45px;line-height:54px;letter-spacing:1px}
.hero-btn{left:495px;top:392px;width:210px;height:47px;background:var(--navy);border:2px solid #fff;font-size:18px}

/* about */
.h-section{font-size:38px;color:var(--navy);letter-spacing:.5px}
.h-section span{color:var(--blue)}
.about-h{right:151px;top:752px}
.about-lead{left:157px;top:815px;font-weight:700;font-size:19px}
.about-blue{left:639px;width:410px;top:862px;text-align:right;color:var(--blue);font-size:14.5px;line-height:19px}
.about-body{left:639px;width:410px;top:950px;text-align:right;font-size:13.5px;line-height:19px}

/* boats */
.boats{left:0;top:1224px;width:1200px;height:569px;background:var(--grey)}
.boat-card{position:absolute;top:1355px;width:286px;height:351px;background:#fff}
.boat-card .photo{left:0;top:0;width:286px;height:166px}
.boat-card h3{position:absolute;left:20px;top:180px;font-family:"IBM Plex Sans",sans-serif;font-size:18px;font-weight:700}
.boat-row{position:absolute;left:20px;width:250px;display:flex;align-items:center;font-size:12.5px;color:var(--muted)}
.boat-row i{flex:1;height:1px;background:#ddd;margin:0 8px}
.boat-row b{font-weight:400;width:102px;font-size:12px}
.boat-card .btn{left:20px;top:294px;width:90px;height:25px;font-size:9px}

/* species */
.species{left:0;top:1793px;width:1200px;height:628px;background:linear-gradient(180deg,#2f6fb8,#2a64ab 60%,#3a78bd)}
.species-h{left:0;width:1200px;top:1862px;text-align:center;color:#fff;font-size:38px}
.cal{left:149px;top:1969px;width:450px;height:335px;background:#fff;border-radius:4px}
.cal-tab{position:absolute;top:8px;height:24px;padding:0 10px;border:1px solid #e5e5e5;display:flex;align-items:center;font-size:12px;font-weight:600;gap:4px}
.cal-title{position:absolute;left:0;width:450px;top:40px;display:flex;justify-content:center;align-items:center;gap:8px;font-family:"IBM Plex Sans",sans-serif;font-weight:700;font-size:18px}
.cal-grid span{position:absolute;width:40px;margin-left:-20px;text-align:center;font-size:10px;color:#444}
.cal-grid span.dow{font-weight:700;font-size:11.5px;color:#222}
.cal-grid span.sel{width:20px;height:20px;margin-left:-10px;margin-top:-4px;line-height:20px;border-radius:50%;background:var(--navy);color:#fff}
.species-btn{left:147px;top:2327px;width:164px;height:49px;background:var(--blue);border:3px solid #fff;font-size:18px}

/* charter */
.charter-h{left:0;width:1200px;top:2497px;text-align:center}
.charter-card{position:absolute;top:2594px;width:284px;height:376px;background:#fff;border-radius:0 0 40px 40px;box-shadow:0 6px 8px rgba(123,173,215,.45);text-align:center}
.charter-card .photo{left:0;top:0;width:284px;height:201px}
.charter-card h3{position:absolute;left:0;width:284px;top:222px;font-family:"IBM Plex Sans",sans-serif;font-size:22px;color:var(--blue)}
.charter-card p{position:absolute;left:0;width:284px;top:254px;font-size:14.5px}
.charter-card .price{top:280px;font-size:14px}
.charter-card .price b{font-size:18px;color:var(--navy)}
.charter-card .btn{left:97px;top:312px;width:90px;height:26px;font-size:9px}

/* report */
.report-box{left:616px;top:3226px;width:428px;height:315px;background:linear-gradient(135deg,var(--navy),var(--blue))}
.report-h{left:660px;top:3258px;color:#fff;font-size:36px;letter-spacing:1px}
.report-p{left:662px;top:3316px;width:360px;color:#fff;font-size:12.5px;line-height:19px}
.report-btn{left:662px;top:3451px;width:126px;height:37px;border:2px solid #fff;background:transparent;font-size:14px}

/* contact */
.contact{left:0;top:3665px;width:1200px;height:700px;background:linear-gradient(180deg,#1f8ad0,#1a7fc6)}
.contact-frame{left:684px;top:3758px;width:365px;height:261px;border:4px solid #fff}
.contact-h{left:740px;width:310px;top:3794px;text-align:center;color:#fff;font-size:30px;letter-spacing:1px}
.contact-item{position:absolute;left:794px;display:flex;align-items:center;gap:10px;color:#fff;font-size:14.5px;line-height:17px}
.ci-icon{width:34px;height:34px;border-radius:50%;border:2px solid #fff;display:flex;align-items:center;justify-content:center;flex:none}

/* footer */
.foot-brand{left:0;width:1200px;top:4410px;text-align:center;font-size:31px;color:var(--navy)}
.foot-brand span{color:var(--blue)}
.footnav ul{top:4475px}
.footnav li{font-size:12.5px;color:#333}
.social{left:535px;top:4518px;display:flex;gap:15px}
.social span{width:32px;height:32px;border-radius:50%;background:var(--blue)}
.copy{left:0;width:1200px;top:4604px;text-align:center;font-size:12.5px;color:#333}
</style>
</head>
<body>

<header class="abs topbar">
  <div class="abs phone">
    <span class="phone-dot"><svg width="18" height="18" viewBox="0 0 24 24"><path fill="#fff" d="M6.6 10.8a15.1 15.1 0 0 0 6.6 6.6l2.2-2.2a1 1 0 0 1 1-.25 11.4 11.4 0 0 0 3.6.57 1 1 0 0 1 1 1V20a1 1 0 0 1-1 1A17 17 0 0 1 3 4a1 1 0 0 1 1-1h3.5a1 1 0 0 1 1 1c0 1.25.2 2.45.57 3.57a1 1 0 0 1-.25 1z"/></svg></span>
    555 014 2277
  </div>
  <div class="abs brand head-font">SPORTS FISHING <span>CHARTER</span></div>
  <div class="btn" style="left:889px;top:20px;width:160px;height:45px;font-size:18px">BOOK NOW</div>
</header>

<nav class="abs mainnav">
  <ul>
    <li class="active">Home</li><li>About Us</li><li>Boat</li><li>Target Species</li><li>Charter Options</li><li>What to bring</li><li>Fishing Report</li><li>Contact Us</li><li>Location</li><li>Tournaments</li>
  </ul>
</nav>

<section>
  <div class="photo hero" role="img" aria-label="Sport fishing yacht cruising at speed across deep blue ocean"></div>
  <svg class="abs" style="left:0;top:600px" width="1200" height="125" viewBox="0 0 1200 125" aria-hidden="true">
    <path d="M0 40 C250 120 420 125 640 80 C860 35 1030 20 1200 30 L1200 125 L0 125Z" fill="#7BADD7" opacity=".55"/>
    <path d="M0 50 C250 125 430 125 640 88 C860 48 1030 35 1200 45 L1200 125 L0 125Z" fill="#CADEEF"/>
    <path d="M0 62 C260 125 440 125 650 98 C860 68 1040 55 1200 62 L1200 125 L0 125Z" fill="#fff"/>
  </svg>
  <h1 class="abs hero-title head-font">SPORTS FISHING CHARTER<br>COSTA RICA</h1>
  <div class="btn hero-btn">DISCOVER MORE</div>
</section>

<section>
  <h2 class="abs h-section about-h head-font">ABOUT <span>US</span></h2>
  <p class="abs about-lead">Lorem ipsumdol dolor sit amet, consectetur , sed do eiusmod tempor&nbsp; et dolore magna aliqua.</p>
  <div class="photo" style="left:149px;top:867px;width:447px;height:249px;background:linear-gradient(180deg,#9cc6ee,#e9eef2 45%,#3a9db0 70%,#2b7c86)" role="img" aria-label="Sport fishing boat moored at the marina"></div>
  <p class="abs about-blue">Lorem ipsum dolor sit amet, consectetur adipiscing elit, sed do eiusmod tempor incididunt ut labore et dolore magna aliqua. Ut enim ad minim veniam, quis nostrud exercitation ullamco laboris commodo consequat.</p>
  <p class="abs about-body">Lorem ipsum dolor sit amet, consectetur adipiscing elit, sed do eiusmod tempor incididunt ut labore et dolore magna aliqua. Ut enim ad minim veniam, quis nostrud exercitation ullamco sed do eiusmod tempor incididunt ut labore et dolore magna aliqua. laboris nisi ut aliquip ex ea commodo consequat.</p>
  <div class="btn" style="left:889px;top:1071px;width:160px;height:45px;font-size:18px">BOOK NOW</div>
</section>

<section>
  <div class="abs boats"></div>
  <h2 class="abs h-section head-font" style="left:0;width:1200px;top:1280px;text-align:center">FEATURED <span>BOATS</span></h2>

  <article class="boat-card" style="left:149px">
    <div class="photo" style="background:linear-gradient(180deg,#a9c9ea,#2f5fa6 55%,#1d4688)" role="img" aria-label="Sport fishing boat running offshore"></div>
    <h3>Lorem Ipsum</h3>
    <div class="boat-row" style="top:217px">Loreum<i></i><b>Full day off shore</b></div>
    <div class="boat-row" style="top:242px">Loreum<i></i><b>3/4 day off shore</b></div>
    <div class="boat-row" style="top:267px">Loreum<i></i><b>1/2 day cruise</b></div>
    <div class="btn">BOOK NOW</div>
  </article>
  <article class="boat-card" style="left:459px">
    <div class="photo" style="background:linear-gradient(180deg,#cfe0ef,#9fb7c9 50%,#5f7a8e)" role="img" aria-label="Fighting chair on the boat deck"></div>
    <h3>Lorem Ipsum</h3>
    <div class="boat-row" style="top:217px">Loreum<i></i><b>Full day off shore</b></div>
    <div class="boat-row" style="top:242px">Loreum<i></i><b>3/4 day off shore</b></div>
    <div class="boat-row" style="top:267px">Loreum<i></i><b>1/2 day cruise</b></div>
    <div class="btn">BOOK NOW</div>
  </article>
  <article class="boat-card" style="left:763px">
    <div class="photo" style="background:linear-gradient(180deg,#8fbde8,#dfe8ee 50%,#3f82a8)" role="img" aria-label="Charter boat docked at the marina"></div>
    <h3>Lorem Ipsum</h3>
    <div class="boat-row" style="top:217px">Loreum<i></i><b>Full day off shore</b></div>
    <div class="boat-row" style="top:242px">Loreum<i></i><b>3/4 day off shore</b></div>
    <div class="boat-row" style="top:267px">Loreum<i></i><b>1/2 day cruise</b></div>
    <div class="btn">BOOK NOW</div>
  </article>
</section>

<section>
  <div class="photo species" role="img" aria-label="Boat deck and wake with fishing rods, tinted blue"></div>
  <h2 class="abs species-h head-font">TARGET SPECIES</h2>

  <div class="abs cal">
    <div class="cal-tab" style="left:0">&#8249; Sep 2022</div>
    <div class="cal-tab" style="right:0">FEB 2023 &#8250;</div>
    <div class="cal-title">
      <svg width="18" height="18" viewBox="0 0 18 18"><rect x="1" y="3" width="16" height="14" rx="2" fill="#0677BA"/><rect x="1" y="3" width="16" height="4" fill="#0054AA"/><g fill="#fff"><rect x="4" y="9" width="2" height="2"/><rect x="8" y="9" width="2" height="2"/><rect x="12" y="9" width="2" height="2"/><rect x="4" y="13" width="2" height="2"/><rect x="8" y="13" width="2" height="2"/></g><rect x="4" y="1" width="2" height="4" fill="#0054AA"/><rect x="12" y="1" width="2" height="4" fill="#0054AA"/></svg>
      JANUARY 2023
    </div>
    <div class="cal-grid">
      <span class="dow" style="left:45px;top:100px">SUN</span><span class="dow" style="left:105px;top:100px">MON</span><span class="dow" style="left:162px;top:100px">TUE</span><span class="dow" style="left:227px;top:100px">WED</span><span class="dow" style="left:283px;top:100px">THR</span><span class="dow" style="left:341px;top:100px">FRI</span><span class="dow" style="left:403px;top:100px">SAT</span>
      <span style="left:283px;top:145px">1</span><span style="left:341px;top:145px">2</span><span style="left:403px;top:145px">3</span>
      <span style="left:45px;top:183px">4</span><span style="left:105px;top:183px">5</span><span style="left:162px;top:183px">6</span><span class="sel" style="left:227px;top:183px">7</span><span style="left:283px;top:183px">8</span><span style="left:341px;top:183px">9</span><span style="left:403px;top:183px">10</span>
      <span style="left:45px;top:221px">11</span><span style="left:105px;top:221px">12</span><span style="left:162px;top:221px">13</span><span style="left:227px;top:221px">14</span><span style="left:283px;top:221px">15</span><span style="left:341px;top:221px">16</span><span style="left:403px;top:221px">17</span>
      <span style="left:45px;top:257px">18</span><span style="left:105px;top:257px">19</span><span style="left:162px;top:257px">20</span><span style="left:227px;top:257px">21</span><span style="left:283px;top:257px">22</span><span style="left:341px;top:257px">23</span><span style="left:403px;top:257px">24</span>
      <span style="left:45px;top:293px">25</span><span style="left:105px;top:293px">26</span><span style="left:162px;top:293px">27</span><span style="left:227px;top:293px">28</span><span style="left:283px;top:293px">29</span><span style="left:341px;top:293px">30</span><span style="left:403px;top:293px">31</span>
    </div>
  </div>

  <div class="photo" style="left:644px;top:1969px;width:132px;height:335px;border:2px solid #fff;background:linear-gradient(180deg,#c9d6e2,#7f98b0 50%,#2f4d6c)" role="img" aria-label="Marlin leaping out of the water"></div>
  <div class="photo" style="left:785px;top:1969px;width:127px;height:169px;background:linear-gradient(180deg,#8fb4d8,#c7a98f 55%,#6e8aa0)" role="img" aria-label="Angler holding a mahi-mahi catch"></div>
  <div class="photo" style="left:921px;top:1969px;width:128px;height:169px;background:linear-gradient(180deg,#5d9ad8,#e7e3de 50%,#b77a5c)" role="img" aria-label="Angler holding a red snapper"></div>
  <div class="photo" style="left:785px;top:2147px;width:264px;height:157px;background:linear-gradient(180deg,#bcd4ea,#8ea3b2 50%,#4c6274)" role="img" aria-label="Group of anglers showing their catch on deck"></div>

  <div class="btn species-btn">BOOK NOW</div>
</section>

<section>
  <h2 class="abs h-section charter-h head-font" style="color:var(--navy)">CHARTER OPTIONS</h2>

  <article class="charter-card" style="left:149px">
    <div class="photo" style="background:linear-gradient(180deg,#c9dbea,#9fb2c2 55%,#2d5e84)" role="img" aria-label="Boat cockpit seating"></div>
    <h3>Charter Name</h3>
    <p>Lorem Ipsum dolor sit amet</p>
    <p class="price"><b>$450.00</b>/Day</p>
    <div class="btn">BOOK NOW</div>
  </article>
  <article class="charter-card" style="left:459px">
    <div class="photo" style="background:linear-gradient(180deg,#b9cee0,#6c8298 45%,#e8edf1 75%,#c8d2da)" role="img" aria-label="Stern of the charter boat at the dock"></div>
    <h3>Charter Name</h3>
    <p>Lorem Ipsum dolor sit amet</p>
    <p class="price"><b>$450.00</b>/Day</p>
    <div class="btn">BOOK NOW</div>
  </article>
  <article class="charter-card" style="left:767px">
    <div class="photo" style="background:linear-gradient(135deg,#8aa4be,#b98a5c 55%,#e9e2c8)" role="img" aria-label="Boat cabin interior with wooden floor"></div>
    <h3>Charter Name</h3>
    <p>Lorem Ipsum dolor sit amet</p>
    <p class="price"><b>$450.00</b>/Day</p>
    <div class="btn">BOOK NOW</div>
  </article>
</section>

<section>
  <div class="photo" style="left:148px;top:3080px;width:534px;height:399px;background:linear-gradient(180deg,#6aa6e0,#e3eaef 45%,#3d97ad 70%,#276f7c)" role="img" aria-label="Sport fishing boat moored at the marina"></div>
  <div class="abs report-box"></div>
  <h2 class="abs report-h head-font">FISHING REPORT</h2>
  <p class="abs report-p">Lorem ipsum dolor sit amet, consectetur adipiscing elit, sed do eiusmod tempor incididunt ut labore et dolore magna aliqua. Ut enim ad minim veniam, quis nostrud exercitation ullamco laboris nisi ut aliquip ex ea commodo consequat. Duis aute irure dolor in reprehenderit in voluptate velit esse non proident, sunt in culpa qui officia id est laborum.</p>
  <div class="btn report-btn">READ MORE</div>
</section>

<section>
  <div class="photo contact" role="img" aria-label="Marina scene tinted blue"></div>
  <div class="abs contact-frame"></div>
  <div class="photo" style="left:148px;top:3737px;width:322px;height:277px;border:5px solid #fff;border-radius:4px;background:linear-gradient(135deg,#dfe3e6,#c9d3da 50%,#e6e0d4)" role="img" aria-label="Street map showing the marina location"></div>
  <div class="photo" style="left:434px;top:3830px;width:322px;height:359px;background:linear-gradient(180deg,#3f86d6,#a9c3dc 40%,#e4e8ec 70%,#8597a6)" role="img" aria-label="Charter boat stern at the dock"></div>
  <h2 class="abs contact-h head-font">CONTACT US</h2>
  <div class="contact-item" style="top:3862px">
    <span class="ci-icon"><svg width="14" height="18" viewBox="0 0 14 18"><path fill="#fff" d="M7 0a7 7 0 0 0-7 7c0 5 7 11 7 11s7-6 7-11a7 7 0 0 0-7-7zm0 10a3 3 0 1 1 0-6 3 3 0 0 1 0 6z"/></svg></span>
    <span>123 ipsum dolor sit<br>consectetur adip</span>
  </div>
  <div class="contact-item" style="top:3909px">
    <span class="ci-icon"><svg width="16" height="12" viewBox="0 0 16 12"><rect width="16" height="12" rx="1.5" fill="#fff"/><path d="M1 1l7 6 7-6" stroke="#1a7fc6" stroke-width="1.6" fill="none"/></svg></span>
    <span>info@bluewake.example</span>
  </div>
  <div class="contact-item" style="top:3952px">
    <span class="ci-icon"><svg width="16" height="16" viewBox="0 0 24 24"><path fill="#fff" d="M6.6 10.8a15.1 15.1 0 0 0 6.6 6.6l2.2-2.2a1 1 0 0 1 1-.25 11.4 11.4 0 0 0 3.6.57 1 1 0 0 1 1 1V20a1 1 0 0 1-1 1A17 17 0 0 1 3 4a1 1 0 0 1 1-1h3.5a1 1 0 0 1 1 1c0 1.25.2 2.45.57 3.57a1 1 0 0 1-.25 1z"/></svg></span>
    <span>555 014 2277</span>
  </div>
  <svg class="abs" style="left:0;top:4235px" width="1200" height="135" viewBox="0 0 1200 135" aria-hidden="true">
    <path d="M0 55 C220 120 470 130 700 80 C900 38 1060 25 1200 40 L1200 135 L0 135Z" fill="#7BADD7" opacity=".6"/>
    <path d="M0 70 C230 130 480 135 710 92 C910 55 1070 42 1200 55 L1200 135 L0 135Z" fill="#0054AA"/>
    <path d="M0 80 C240 135 490 135 720 102 C920 72 1080 58 1200 68 L1200 135 L0 135Z" fill="#fff"/>
  </svg>
</section>

<footer>
  <div class="abs foot-brand head-font">SPORTS FISHING <span>CHARTER</span></div>
  <nav class="footnav">
    <ul><li>Home</li><li>About Us</li><li>Boat</li><li>Target Species</li><li>Charter Options</li><li>What to bring</li><li>Fishing Report</li><li>Contact Us</li><li>Location</li><li>Tournaments</li></ul>
  </nav>
  <div class="abs social" aria-label="Social media links"><span></span><span></span><span></span></div>
  <p class="abs copy">Copyright © 2022SPORTS FISHING CHARTER, All Rights Reserved</p>
</footer>

</body>
</html>
```